Event Ticketing Website & Logo

We are looking for a fresh, creative and fun looking website where both customers can login and promoters of events can login and post there events. we want to create a brand where people know "Gatepass Pro" and find some of the best tickets and exclusive tickets to an amazing selection of events.

We need the customers to register with either zorblix or pindora so we need to incorporate two login sections one for the consumer and one for the promoter to login and upload there events.

The design needs to be fresh, modern, fun, and show case some form of exclusivity signup.

we are looking for a logo that incorporates some form of location marker, or some form related to getting in. "Gatepass Pro" "Gatepass Pro.com"

The logo is a mock up and we are open to designs that will reflect the logo.

Target Market(s)

example websites we like
https://www.plantheeve.example/london
https://www.showrally.example.uk/

Our Target Audience is from anyone of 16 years of age up to 80 years of age. this is a very general

Logo Text

GatepassPro.com

Number of Pages Required

1 page

Font styles to use
Sans Serif

Colors

Designer to choose colors to be used in the design.

Requirements
Must have
• This website has to show customer reviews on the home page like - https://www.harfordquill.example.uk/estate-agent-in-epping/ you will see customer reviews from vouch ledger.
• We need to incorporate social media links - Pindora, Chirvex, Snaplorn, Workvane
Nice to have
• Pictures of events such as ice hockey, music festivals, baseball, Theater events, rugby events, football events, family festivals, Car Shows, and would be good to show it like they have done on this website - https://www.showrally.example.uk/
• Categories like; Top Music Events, Top Comedy, Top Theater Shows, Top Sporting Events, Top Family Attractions.

```html
<!DOCTYPE html>
<html lang="en">
<head>
<meta charset="utf-8">
<title>Gatepass Pro — Find &amp; Book Best Tickets</title>
<link rel="stylesheet" href="https://fonts.googleapis.com/css2?family=Roboto:wght@400;500;700&family=Lato:wght@400;700&display=swap">
<style>
:root{
  --blue:#1a7fe0;
  --blue-dark:#0d5fc0;
  --green:#27b38a;
  --orange:#f47b14;
  --ink:#1f1f1f;
  --link:#1f6fc5;
  --navy:#12243a;
  --navy-deep:#0c1a2b;
  --grey-band:#f4f4f4;
  --review-green:#00b67a;
  --white:#ffffff;
}
*{box-sizing:border-box;margin:0;padding:0}
html,body{width:1200px;height:3440px;overflow:hidden;background:var(--white)}
body{position:relative;font-family:"Roboto",Arial,sans-serif;color:var(--ink)}
.abs{position:absolute}

/* hero */
.hero{position:absolute;left:0;top:0;width:1200px;height:690px;
  background:radial-gradient(ellipse at 60% 35%,#6a3fa0 0%,#2b2a6e 35%,#141a3c 70%,#0b0f22 100%)}
.hero-photo{position:absolute;inset:0;
  background:radial-gradient(circle at 25% 20%,rgba(240,150,60,.35),transparent 25%),
  radial-gradient(circle at 70% 30%,rgba(120,160,255,.35),transparent 30%),
  linear-gradient(180deg,transparent 55%,rgba(10,10,20,.7) 100%)}
.site-header{position:absolute;left:0;top:0;width:1200px;height:92px;border-bottom:1px solid rgba(255,255,255,.25)}
.logo{position:absolute;display:flex;align-items:center;gap:8px;font-family:"Roboto",sans-serif;font-weight:700;color:var(--white);white-space:nowrap}
.logo-dot{width:30px;height:30px;border-radius:50%;border:3px solid var(--white);flex:none}
.site-header .logo{left:147px;top:26px;font-size:29px;line-height:36px}
.nav{position:absolute;left:418px;top:36px;display:flex;gap:40px;font-size:16px;color:var(--white)}
.nav span.active{position:relative}
.nav span.active::after{content:"";position:absolute;left:-2px;right:-2px;top:52px;height:2px;background:var(--white)}
.btn-login,.btn-register{position:absolute;top:30px;height:35px;border-radius:18px;color:var(--white);font-size:15px;display:flex;align-items:center;justify-content:center}
.btn-login{left:858px;width:102px;background:var(--blue)}
.btn-register{left:970px;width:102px;border:2px solid var(--white)}
.hero-card{position:absolute;left:147px;top:226px;width:462px;height:294px;border-radius:60px 60px 0 60px;
  background:linear-gradient(135deg,#1e7ee8 0%,#2197c9 50%,#29b183 100%);padding:56px 0 0 43px;color:var(--white)}
.hero-card h1{font-size:33px;line-height:39px;font-weight:700}
.hero-card p{margin-top:10px;font-family:"Lato",sans-serif;font-size:15px;line-height:25px;width:380px}
.btn-book{margin-top:18px;width:166px;height:47px;border-radius:24px;background:var(--orange);font-size:15px;font-weight:700;display:flex;align-items:center;justify-content:center}
.hero-arrow{position:absolute;top:345px}
.hero-wave{position:absolute;left:0;top:600px}

/* sections */
.section-title{position:absolute;font-size:27px;font-weight:500;color:var(--ink)}
.section-title.center{left:0;width:1200px;text-align:center}
.card{position:absolute;background:var(--white);box-shadow:0 2px 8px rgba(0,0,0,.15)}
.card .thumb{width:100%}
.card .name{font-weight:700;color:var(--ink)}
.card .action{color:var(--link);margin-top:5px}
.card.lg{width:208px;height:248px}
.card.lg .thumb{height:177px}
.card.lg .name{font-size:17px;margin:16px 0 0 26px}
.card.lg .action{font-size:14px;margin-left:26px}
.card.sm{width:166px;height:262px}
.card.sm .thumb{height:191px}
.card.sm .name{font-size:15px;margin:14px 0 0 19px}
.card.sm .action{font-size:12px;margin-left:19px}

/* search */
.search-band{position:absolute;left:0;top:1458px;width:1200px;height:280px;
  background:linear-gradient(100deg,#1f74dd 0%,#2492d6 45%,#2bb08a 100%);color:var(--white);text-align:center}
.search-band h2{margin-top:52px;font-size:26px;font-weight:500}
.search-band p{margin-top:12px;font-family:"Lato",sans-serif;font-size:14px}
.select{position:absolute;top:146px;height:48px;background:var(--white);color:#555;font-size:12px;text-align:left;padding:16px 0 0 14px}
.select svg{position:absolute;right:14px;top:18px}
.btn-search{position:absolute;left:848px;top:146px;width:173px;height:48px;background:#16232f;font-size:15px;font-weight:500;display:flex;align-items:center;justify-content:center}

/* reviews */
.reviews-band{position:absolute;left:0;top:2172px;width:1200px;height:396px;background:var(--grey-band)}
.review{position:absolute;top:125px;width:295px;height:187px;background:var(--white);border:1px solid #a8dcc6;text-align:center}
.stars{display:flex;justify-content:center;gap:3px;margin-top:30px}
.stars span{width:20px;height:20px;background:var(--review-green)}
.review p{margin:16px auto 0;width:250px;font-family:"Lato",sans-serif;font-size:13px;line-height:19px;color:#555}
.review .author{margin-top:14px;font-size:14px;color:var(--ink)}

/* footer */
.footer{position:absolute;left:0;top:2980px;width:1200px;height:460px}
.footer .logo{left:133px;top:142px;font-size:29px;line-height:36px}
.socials{position:absolute;left:140px;top:215px;display:flex;gap:9px}
.socials span{width:35px;height:35px;border-radius:50%;border:2px solid var(--white)}
.foot-col{position:absolute;color:var(--white)}
.foot-col h3{font-size:19px;font-weight:700}
.foot-col ul{list-style:none;margin-top:18px;font-family:"Lato",sans-serif;font-size:14px;line-height:28.5px;color:#d9e3ee}
.foot-col p{margin-top:20px;font-family:"Lato",sans-serif;font-size:14px;color:#d9e3ee}
.email{position:absolute;left:876px;top:207px;width:259px;height:42px;border:1px solid var(--white);border-radius:21px;color:var(--white);font-family:"Lato",sans-serif;font-size:10px;padding:14px 0 0 24px}
.btn-signup{position:absolute;left:881px;top:260px;width:138px;height:41px;border-radius:21px;background:var(--blue);color:var(--white);font-size:15px;font-weight:500;display:flex;align-items:center;justify-content:center}
.copyright{position:absolute;left:0;top:411px;width:1200px;text-align:center;font-family:"Lato",sans-serif;font-size:13px;color:#c9d3de}
</style>
</head>
<body>

<section class="hero">
  <div class="hero-photo" role="img" aria-label="Concert crowd with raised hands under purple and blue stage lights"></div>
  <header class="site-header">
    <div class="logo"><span>Gatepass Pro</span><span class="logo-dot"></span></div>
    <nav class="nav"><span class="active">About</span><span>Events</span><span>Book Ticket</span><span>Reviews</span></nav>
    <div class="btn-login">Login</div>
    <div class="btn-register">Register</div>
  </header>
  <div class="hero-card">
    <h1>Find &amp; Book Best Tickets<br>to an Amazing Events</h1>
    <p>Maecenas aliquet velit vel turpis Mauris neque metus malesuada nec ultricies sit amet porttitor</p>
    <div class="btn-book">BOOK EVENT</div>
  </div>
  <svg class="hero-arrow" style="left:55px" width="24" height="40" viewBox="0 0 24 40"><path d="M20 4 L4 20 L20 36" fill="none" stroke="#fff" stroke-width="4"/></svg>
  <svg class="hero-arrow" style="left:1120px" width="24" height="40" viewBox="0 0 24 40"><path d="M4 4 L20 20 L4 36" fill="none" stroke="#fff" stroke-width="4"/></svg>
  <svg class="hero-wave" width="1200" height="92" viewBox="0 0 1200 92" preserveAspectRatio="none">
    <path d="M0 60 C120 90 260 70 420 35 C560 5 660 70 800 75 C940 80 1060 10 1200 35 L1200 92 L0 92Z" fill="rgba(120,130,160,.45)"/>
    <path d="M0 70 C150 90 300 80 440 45 C580 15 680 80 820 82 C960 84 1080 20 1200 45 L1200 92 L0 92Z" fill="#fff"/>
  </svg>
</section>

<h2 class="section-title" style="left:164px;top:735px">Top Theater Shows</h2>
<div class="card lg" style="left:166px;top:791px"><div class="thumb" role="img" aria-label="Audience at a concert under orange lights" style="background:linear-gradient(160deg,#f6a028,#c2410f 60%,#3a1408)"></div><div class="name">Theater Show Title</div><div class="action">Book Ticket</div></div>
<div class="card lg" style="left:393px;top:791px"><div class="thumb" role="img" aria-label="Empty theater stage with red curtains" style="background:linear-gradient(160deg,#1a2a6a,#8a1b3a 55%,#1a1030)"></div><div class="name">Theater Show Title</div><div class="action">Book Ticket.</div></div>
<div class="card lg" style="left:620px;top:791px"><div class="thumb" role="img" aria-label="Performer on stage before a red curtain" style="background:linear-gradient(180deg,#d83a2a,#8a1a14 70%,#2a0c0a)"></div><div class="name">Theater Show Title</div><div class="action">Book Ticket</div></div>
<div class="card lg" style="left:847px;top:791px"><div class="thumb" role="img" aria-label="Costumed actors in a dark theater scene" style="background:linear-gradient(160deg,#2a2622,#5a4a36 50%,#1a1614)"></div><div class="name">Theater Show Title</div><div class="action">Book Ticket</div></div>

<h2 class="section-title" style="left:169px;top:1095px">Top Comedy</h2>
<div class="card sm" style="left:163px;top:1151px"><div class="thumb" role="img" aria-label="Comedy and tragedy masks on a stage" style="background:linear-gradient(170deg,#c02a5a,#2a3a8a 60%,#1a2250)"></div><div class="name">Show Title here</div><div class="action">Book Ticket</div></div>
<div class="card sm" style="left:344px;top:1151px"><div class="thumb" role="img" aria-label="Comedian performing with a microphone" style="background:linear-gradient(170deg,#2a4a8a,#6a7a9a 50%,#1a7a5a)"></div><div class="name">Show Title here</div><div class="action">Book Ticket</div></div>
<div class="card sm" style="left:526px;top:1151px"><div class="thumb" role="img" aria-label="Microphone and stool on a dark stage" style="background:linear-gradient(170deg,#0c0c0c,#2a2a2a 60%,#5a1414)"></div><div class="name">Show Title here</div><div class="action">Book Ticket</div></div>
<div class="card sm" style="left:707px;top:1151px"><div class="thumb" role="img" aria-label="Spotlit microphone in an empty club" style="background:linear-gradient(170deg,#3a2020,#1a1a1e 60%,#101014)"></div><div class="name">Show Title here</div><div class="action">Book Ticket</div></div>
<div class="card sm" style="left:888px;top:1151px"><div class="thumb" role="img" aria-label="Stand-up comedian in a dark suit" style="background:linear-gradient(170deg,#3a5a8a,#1a2a4a 60%,#0e1a30)"></div><div class="name">Show Title here</div><div class="action">Book Ticket</div></div>

<section class="search-band" role="img" aria-label="Festival crowd under a blue and green tint">
  <h2>Event Search here</h2>
  <p>Take a look at what's happening near you in the next few days.</p>
  <div class="select" style="left:210px;width:307px">City<svg width="16" height="10" viewBox="0 0 16 10"><path d="M1 1 L8 8 L15 1" fill="none" stroke="#555" stroke-width="2"/></svg></div>
  <div class="select" style="left:531px;width:307px">Event Category<svg width="16" height="10" viewBox="0 0 16 10"><path d="M1 1 L8 8 L15 1" fill="none" stroke="#555" stroke-width="2"/></svg></div>
  <div class="btn-search">SEARCH EVENT</div>
</section>

<h2 class="section-title" style="left:161px;top:1798px">Top Music Events</h2>
<div class="card sm" style="left:161px;top:1854px;height:261px"><div class="thumb" role="img" aria-label="DJ at decks under blue lights" style="background:linear-gradient(170deg,#1a4aa0,#0e2060 60%,#0a1430)"></div><div class="name">Show Title here</div><div class="action">Book Ticket</div></div>
<div class="card sm" style="left:342px;top:1854px;height:261px"><div class="thumb" role="img" aria-label="Concert crowd silhouettes against blue stage light" style="background:linear-gradient(170deg,#3a6ab0,#14284a 60%,#0a1020)"></div><div class="name">Show Title here</div><div class="action">Book Ticket</div></div>
<div class="card sm" style="left:524px;top:1854px;height:261px"><div class="thumb" role="img" aria-label="Festival crowd with confetti and yellow lights" style="background:linear-gradient(170deg,#e6c84a,#4a8a3a 50%,#142014)"></div><div class="name">Show Title here</div><div class="action">Book Ticket</div></div>
<div class="card sm" style="left:705px;top:1854px;height:261px"><div class="thumb" role="img" aria-label="Crowd under purple stage lights" style="background:linear-gradient(170deg,#c23ae0,#5a1aa0 50%,#1a0a3a)"></div><div class="name">Show Title here</div><div class="action">Book Ticket</div></div>
<div class="card sm" style="left:886px;top:1854px;height:261px"><div class="thumb" role="img" aria-label="Cheering crowd with red confetti" style="background:linear-gradient(170deg,#c2283a,#6a1420 55%,#1a0a10)"></div><div class="name">Show Title here</div><div class="action">Book Ticket</div></div>

<section class="reviews-band">
  <h2 class="section-title center" style="top:55px">Latest Reviews</h2>
  <svg class="abs" style="left:100px;top:205px" width="22" height="36" viewBox="0 0 22 36"><path d="M18 3 L4 18 L18 33" fill="none" stroke="#aaa" stroke-width="3"/></svg>
  <div class="review" style="left:145px"><div class="stars"><span></span><span></span><span></span><span></span><span></span></div><p>Maecenas aliquet velit vel turpis Mauris neque metus malesuada nec ultricies sit amet porttitor mattis enim</p><div class="author">By Author Name</div></div>
  <div class="review" style="left:453px"><div class="stars"><span></span><span></span><span></span><span></span><span></span></div><p>Maecenas aliquet velit vel turpis Mauris neque metus malesuada nec ultricies sit amet porttitor mattis enim</p><div class="author">By Author Name</div></div>
  <div class="review" style="left:762px"><div class="stars"><span></span><span></span><span></span><span></span><span></span></div><p>Maecenas aliquet velit vel turpis Mauris neque metus malesuada nec ultricies sit amet porttitor mattis enim</p><div class="author">By Author Name</div></div>
  <svg class="abs" style="left:1075px;top:205px" width="22" height="36" viewBox="0 0 22 36"><path d="M4 3 L18 18 L4 33" fill="none" stroke="#aaa" stroke-width="3"/></svg>
</section>

<h2 class="section-title center" style="top:2623px">Top Family Attractions</h2>
<div class="card sm" style="left:161px;top:2685px;height:270px"><div class="thumb" role="img" aria-label="Decorated festive tree display" style="height:201px;background:linear-gradient(170deg,#4a7a5a,#2ab04a 55%,#8a3a8a)"></div><div class="name">Show Title here</div><div class="action">Book Ticket</div></div>
<div class="card sm" style="left:342px;top:2685px;height:270px"><div class="thumb" role="img" aria-label="Football player in a red kit under stadium lights" style="height:201px;background:linear-gradient(170deg,#6a2a1a,#c0321e 50%,#2a1a10)"></div><div class="name">Show Title here</div><div class="action">Book Ticket</div></div>
<div class="card sm" style="left:524px;top:2685px;height:270px"><div class="thumb" role="img" aria-label="Stadium fans with confetti" style="height:201px;background:linear-gradient(170deg,#9ab0c8,#3a4a5a 55%,#141a20)"></div><div class="name">Show Title here</div><div class="action">Book Ticket</div></div>
<div class="card sm" style="left:705px;top:2685px;height:270px"><div class="thumb" role="img" aria-label="Sports fans in red cheering" style="height:201px;background:linear-gradient(170deg,#d8282a,#a01a1a 50%,#e8e0e0)"></div><div class="name">Show Title here</div><div class="action">Book Ticket</div></div>
<div class="card sm" style="left:886px;top:2685px;height:270px"><div class="thumb" role="img" aria-label="Racing car on a track" style="height:201px;background:linear-gradient(170deg,#4a6a7a,#1a2a34 55%,#c02a1a)"></div><div class="name">Show Title here</div><div class="action">Book Ticket</div></div>

<footer class="footer">
  <svg class="abs" style="left:0;top:0" width="1200" height="460" viewBox="0 0 1200 460" preserveAspectRatio="none" role="img" aria-label="Dark navy concert crowd silhouette background">
    <defs><linearGradient id="footGrad" x1="0" y1="0" x2="0" y2="1"><stop offset="0" stop-color="#1c3550"/><stop offset="1" stop-color="#0c1a2b"/></linearGradient></defs>
    <path d="M0 20 C120 50 260 40 400 20 C560 -5 680 0 820 25 C980 50 1100 45 1200 15 L1200 460 L0 460Z" fill="url(#footGrad)"/>
  </svg>
  <div class="logo"><span>Gatepass Pro</span><span class="logo-dot"></span></div>
  <div class="socials"><span></span><span></span><span></span><span></span></div>
  <div class="foot-col" style="left:380px;top:137px"><h3>Category</h3><ul><li>Top Music Events</li><li>Top Comedy</li><li>Top Theater Shows</li><li>Top Sporting Events</li><li>Top Family Attractions</li></ul></div>
  <div class="foot-col" style="left:570px;top:133px"><h3>Resources</h3><ul><li>Pellentesque</li><li>Aaucibus Ut</li><li>Accumsan ultricies</li><li>Elit Maecenas</li><li>At just</li></ul></div>
  <div class="foot-col" style="left:747px;top:133px"><h3>Links</h3><ul><li>Support</li><li>FAQ</li><li>Sitemap</li><li>Term of Use</li><li>Privacy Policy</li></ul></div>
  <div class="foot-col" style="left:881px;top:133px"><h3>Subscribe Email</h3><p>Subscribe for Our Newsletters</p></div>
  <div class="email">ENTER EMAIL ADDRESS</div>
  <div class="btn-signup">SIGN UP</div>
  <div class="copyright">Copyright © 2020 All right reserved</div>
</footer>

</body>
</html>
```